Wedding Welcome Sign

Require a wedding welcome sign with wording as attached in picture
We are after something sophisticated, classy and elegant (simple and understated yet catchy)

Will be printed onto a mirror
Size of writing to cover 680mm high x 430mm wide

```html
<!DOCTYPE html>
<html lang="en">
<head>
<meta charset="utf-8">
<title>Wedding Welcome Sign</title>
<link rel="stylesheet" href="https://fonts.googleapis.com/css2?family=Dancing+Script:wght@400;700&display=swap">
<style>
  :root {
    --ink: #111111;
    --paper: #ffffff;
    --ornament-fill: #d9d9d9;
  }
  html, body {
    margin: 0;
    padding: 0;
    width: 1200px;
    height: 1200px;
    overflow: hidden;
    background: var(--paper);
  }
  .sign {
    position: relative;
    width: 1200px;
    height: 1200px;
    color: var(--ink);
    font-family: "Dancing Script", cursive;
    text-align: center;
  }
  .line {
    position: absolute;
    left: 0;
    width: 1200px;
    margin: 0;
    line-height: 1;
    font-weight: 400;
  }
  .ornament {
    position: absolute;
    left: 560px;
    width: 96px;
    height: 88px;
  }
  .ornament--top { top: 24px; }
  .ornament--bottom { top: 1075px; }
  .vow { font-size: 64px; }
  .vow--love { font-weight: 700; font-size: 58px; }
  .welcome { font-size: 64px; }
  .couple { font-size: 72px; }
  .date { font-size: 46px; font-weight: 700; }
  .date__month { font-size: 34px; font-weight: 400; }
</style>
</head>
<body>
<main class="sign">
  <svg class="ornament ornament--top" viewBox="0 0 96 88" role="img" aria-label="Celtic knot heart ornament">
    <path d="M48 84 C20 62 4 46 4 26 C4 12 15 4 27 4 C37 4 44 10 48 18 C52 10 59 4 69 4 C81 4 92 12 92 26 C92 46 76 62 48 84 Z" fill="var(--ornament-fill)"/>
  </svg>

  <p class="line vow" style="top:193px">Today I marry my</p>
  <p class="line vow" style="top:252px">best friend. The one</p>
  <p class="line vow" style="top:310px">I laugh with, live for,</p>
  <p class="line vow" style="top:368px">dream with,</p>
  <p class="line vow vow--love" style="top:424px">love.</p>

  <p class="line welcome" style="top:603px">Welcome to our</p>
  <p class="line welcome" style="top:670px">wedding</p>

  <p class="line couple" style="top:808px">Daniel &amp; Harriet</p>

  <p class="line date" style="top:955px">20 <span class="date__month">May</span> 2017</p>

  <svg class="ornament ornament--bottom" viewBox="0 0 96 88" role="img" aria-label="Celtic knot heart ornament">
    <path d="M48 84 C20 62 4 46 4 26 C4 12 15 4 27 4 C37 4 44 10 48 18 C52 10 59 4 69 4 C81 4 92 12 92 26 C92 46 76 62 48 84 Z" fill="var(--ornament-fill)"/>
  </svg>
</main>
</body>
</html>
```